"Drink Champagne and Dance on the Table" sort of business card needed!

We throw events, weddings, engagement parties, baby showers and the sort of end of year corporate events that people remember long after the glitter has settled - the sort of events that make you stand still and say wow when you walk in and then make you want to "Drink Champagne and Dance on the Tables"

We have a great logo with heaps of potential and need a business card that just screams creative professionals!

We are based in Auckland, NZ and are priced at the Premium end of the market were there are around 10 other main competitors. We need to stand out and make a strong statement about who we are!

Our Business Card will be one of the few items that we print out so are fully prepared to invest in a premium print job.

We really love our logo and think it has heaps of potential! Its ok if you would like to manipulate it (maybe put it on an angle, or use the circle element on its own?).

Black and Gold is very striking, but its very done in our market so we would like to avoid a solid black background please

We have done a bit of an inspiration document to give you an idea of the sort of look and feel we are hoping to achieve.

Target Market(s)

Woman aged 30 - 45 with an income bracket of $70k +

Industry/Entity Type

Event Planning

Contact Information for Business Card

Marnie
hello@fennwhistle.co.nz
www.fennwhistle.co.nz
02739418207

Number of Pages Required

5+ page

Requirements
Must have
• Vibrant colours and design (we love the vibrant pink and gold in the inspiration file)
• We would love to see some colour and creativity (although the black and gold is very striking). Because we are doing such minimal print work I am happy for the cards to be a little more expensive so if you want to use cut outs, rounded corners, gold foil, non standard size etc I am happy for that too. I really want the wow factor.
Nice to have
• We would like the design to be double sided.
Should not have
• The logo colour changed
• Use of Purple or Green or solid black background.
• Wedding Photos!

```html
<!DOCTYPE html>
<html lang="en">
<head>
<meta charset="utf-8">
<title>Fenn and Whistle – Business Card Concepts</title>
<link rel="stylesheet" href="https://fonts.googleapis.com/css2?family=Raleway:wght@400;500;600&display=swap">
<style>
  :root {
    --page: #e4e5e1;
    --yellow: #f5c84c;
    --gold: #c9a043;
    --grey: #737573;
    --silver: #d4d4d4;
    --red: #c0152f;
    --ink: #3b3431;
    --white: #ffffff;
  }
  * { margin: 0; padding: 0; box-sizing: border-box; }
  html, body { width: 1200px; height: 1200px; overflow: hidden; background: var(--page); }
  body { position: relative; font-family: "Raleway", sans-serif; }

  .card {
    position: absolute;
    width: 508px;
    height: 284px;
    overflow: hidden;
    box-shadow: 2px 3px 4px rgba(0,0,0,.28);
  }
  .card svg.card-art { position: absolute; inset: 0; width: 100%; height: 100%; display: block; }
  .col-left { left: 73px; }
  .col-right { left: 619px; }
  .row-1 { top: 114px; }
  .row-2 { top: 433px; }
  .row-3 { top: 751px; }

  /* brand lockup */
  .brand {
    position: absolute;
    width: 220px;
    margin-left: -110px;
    text-align: center;
  }
  .brand-ring {
    display: block;
    width: 96px;
    height: 96px;
    margin: 0 auto;
    border: 2px solid var(--gold);
    border-radius: 50%;
  }
  .brand-name {
    display: block;
    margin-top: 14px;
    font-weight: 500;
    font-size: 23px;
    letter-spacing: .5px;
    color: var(--gold);
    white-space: nowrap;
  }

  /* contact block */
  .contact { position: absolute; width: 230px; }
  .contact-name {
    font-weight: 600;
    font-size: 26px;
    line-height: 30px;
    color: var(--red);
    letter-spacing: .3px;
  }
  .contact-rule {
    height: 3px;
    background: var(--yellow);
    margin: 4px 0 6px;
  }
  .contact-line {
    font-size: 15px;
    line-height: 26.5px;
    color: var(--ink);
    white-space: nowrap;
  }
  .contact.centered { text-align: center; }
  .contact.on-dark .contact-line { color: #eeeeee; }
</style>
</head>
<body>

<!-- Front A: yellow ornament with arched white window -->
<section class="card col-left row-1">
  <svg class="card-art" viewBox="0 0 508 284" aria-hidden="false">
    <defs>
      <linearGradient id="frontAOrn" x1="0" y1="0" x2="0" y2="1">
        <stop offset="0" stop-color="#f5c84c"/>
        <stop offset=".6" stop-color="#d9b24c"/>
        <stop offset="1" stop-color="#f3cf6a"/>
      </linearGradient>
    </defs>
    <rect width="508" height="284" fill="url(#frontAOrn)" role="img" aria-label="Gold and grey damask flourish pattern"/>
    <circle cx="255" cy="34" r="212" fill="#ffffff"/>
    <circle cx="255" cy="34" r="208" fill="#737573"/>
    <circle cx="255" cy="34" r="198" fill="#ffffff"/>
  </svg>
  <div class="brand" style="left:247px; top:26px;">
    <span class="brand-ring"></span>
    <span class="brand-name">Fenn and Whistle</span>
  </div>
</section>

<!-- Back A: white with curved grey ornament edge -->
<section class="card col-right row-1">
  <svg class="card-art" viewBox="0 0 508 284">
    <defs>
      <radialGradient id="backAOrn" cx=".75" cy=".5" r=".35">
        <stop offset="0" stop-color="#e8bf4e"/>
        <stop offset=".7" stop-color="#c9a94f"/>
        <stop offset="1" stop-color="#737573"/>
      </radialGradient>
    </defs>
    <rect width="508" height="284" fill="#737573"/>
    <rect x="290" y="0" width="180" height="284" fill="url(#backAOrn)" role="img" aria-label="Gold damask medallion ornament"/>
    <rect width="147" height="284" fill="#ffffff"/>
    <circle cx="147" cy="142" r="192" fill="#ffffff"/>
    <circle cx="147" cy="142" r="188" fill="#737573"/>
    <circle cx="147" cy="142" r="178" fill="#ffffff"/>
  </svg>
  <div class="contact" style="left:60px; top:87px;">
    <div class="contact-name">MARNIE</div>
    <div class="contact-rule"></div>
    <div class="contact-line">02739418207</div>
    <div class="contact-line">hello@fennwhistle.co.nz</div>
    <div class="contact-line">www.fennwhistle.co.nz</div>
  </div>
</section>

<!-- Front B: white panel framed by ornament strips -->
<section class="card col-left row-2" style="background:var(--grey);">
  <svg class="card-art" viewBox="0 0 508 284">
    <defs>
      <linearGradient id="stripOrn" x1="0" y1="0" x2="1" y2="0">
        <stop offset="0" stop-color="#f5c84c"/>
        <stop offset=".5" stop-color="#d9b552"/>
        <stop offset="1" stop-color="#f5c84c"/>
      </linearGradient>
    </defs>
    <g role="img" aria-label="Gold floral scroll pattern strips">
      <rect x="19" y="0" width="50" height="284" fill="url(#stripOrn)"/>
      <rect x="19" y="231" width="95" height="53" fill="url(#stripOrn)"/>
      <rect x="439" y="0" width="48" height="284" fill="url(#stripOrn)"/>
      <rect x="393" y="231" width="94" height="53" fill="url(#stripOrn)"/>
    </g>
    <rect x="69" y="0" width="370" height="229" fill="#ffffff"/>
  </svg>
  <div class="brand" style="left:254px; top:36px;">
    <span class="brand-ring"></span>
    <span class="brand-name">Fenn and Whistle</span>
  </div>
</section>

<!-- Back B: white centre between ornament bands -->
<section class="card col-right row-2" style="background:var(--white);">
  <svg class="card-art" viewBox="0 0 508 284">
    <defs>
      <linearGradient id="bandOrn" x1="0" y1="0" x2="0" y2="1">
        <stop offset="0" stop-color="#8a8266"/>
        <stop offset=".5" stop-color="#d8b650"/>
        <stop offset="1" stop-color="#8a8266"/>
      </linearGradient>
    </defs>
    <rect x="0" y="0" width="508" height="47" fill="url(#bandOrn)" role="img" aria-label="Gold scrolling vine border"/>
    <rect x="0" y="47" width="508" height="11" fill="#f5c84c"/>
    <rect x="0" y="224" width="508" height="10" fill="#f5c84c"/>
    <rect x="0" y="234" width="508" height="50" fill="url(#bandOrn)" role="img" aria-label="Gold scrolling vine border"/>
  </svg>
  <div class="contact centered" style="left:139px; top:82px;">
    <div class="contact-name">MARNIE</div>
    <div class="contact-rule"></div>
    <div class="contact-line">02739418207</div>
    <div class="contact-line">hello@fennwhistle.co.nz</div>
    <div class="contact-line">www.fennwhistle.co.nz</div>
  </div>
</section>

<!-- Front C: grey with gold and silver flourishes -->
<section class="card col-left row-3" style="background:var(--grey);">
  <svg class="card-art" viewBox="0 0 508 284">
    <defs>
      <radialGradient id="goldTL" cx="0" cy=".2" r=".55">
        <stop offset="0" stop-color="#f5c84c"/>
        <stop offset="1" stop-color="#737573" stop-opacity="0"/>
      </radialGradient>
      <radialGradient id="goldBR" cx="1" cy=".8" r=".55">
        <stop offset="0" stop-color="#f5c84c"/>
        <stop offset="1" stop-color="#737573" stop-opacity="0"/>
      </radialGradient>
      <radialGradient id="silverSoft" cx=".5" cy=".5" r=".5">
        <stop offset="0" stop-color="#b3b3b3"/>
        <stop offset="1" stop-color="#737573" stop-opacity="0"/>
      </radialGradient>
    </defs>
    <g role="img" aria-label="Gold swirl flourishes and silver damask medallions">
      <rect width="508" height="284" fill="url(#goldTL)"/>
      <rect width="508" height="284" fill="url(#goldBR)"/>
      <ellipse cx="370" cy="30" rx="100" ry="55" fill="url(#silverSoft)"/>
      <ellipse cx="110" cy="250" rx="100" ry="55" fill="url(#silverSoft)"/>
    </g>
  </svg>
  <div class="brand" style="left:247px; top:73px;">
    <span class="brand-ring"></span>
    <span class="brand-name">Fenn and Whistle</span>
  </div>
</section>

<!-- Back C: grey panel between silver strips -->
<section class="card col-right row-3" style="background:var(--grey);">
  <svg class="card-art" viewBox="0 0 508 284">
    <defs>
      <linearGradient id="silverOrn" x1="0" y1="0" x2="1" y2="0">
        <stop offset="0" stop-color="#f2f2f2"/>
        <stop offset=".5" stop-color="#c9c9c9"/>
        <stop offset="1" stop-color="#f2f2f2"/>
      </linearGradient>
    </defs>
    <rect x="0" y="0" width="66" height="284" fill="url(#silverOrn)" role="img" aria-label="Silver damask pattern strip"/>
    <rect x="66" y="0" width="10" height="284" fill="#f5c84c"/>
    <rect x="432" y="0" width="10" height="284" fill="#f5c84c"/>
    <rect x="442" y="0" width="66" height="284" fill="url(#silverOrn)" role="img" aria-label="Silver damask pattern strip"/>
  </svg>
  <div class="contact on-dark" style="left:159px; top:82px;">
    <div class="contact-name">MARNIE</div>
    <div class="contact-rule"></div>
    <div class="contact-line">02739418207</div>
    <div class="contact-line">hello@fennwhistle.co.nz</div>
    <div class="contact-line">www.fennwhistle.co.nz</div>
  </div>
</section>

</body>
</html>
```